Marketing Postcard Design for a Medical Supply Company

We are sending a marketing postcard to healthcare facilities within our state. We are in need of a design for a 6"x9" postcard, front and back with our logo, website www.carevale.shop, phone number 808-241-7739, and 12 products. The products are face shields, nitrile gloves, vinyl gloves, isolation gowns, gallon hand sanitizer, black KN95's, white KN95's, 4520 N95, 4530 N95, biohazard bags, Puratex wipes, and Kor spray. All of these items can be found on our website at carevale.shop. Please include a promo code, 10OFF for 10% Off. The design should be clean, professional, and appeal to a healthcare or medical audience.

```html
<!DOCTYPE html>
<html lang="en">
<head>
<meta charset="utf-8">
<title>Carevale Medical Supply – Postcard</title>
<link rel="stylesheet" href="https://fonts.googleapis.com/css2?family=Montserrat:ital,wght@0,400;0,500;0,600;0,700;0,800;0,900;1,700&display=swap">
<style>
  :root {
    --green: #1f9b40;
    --green-dark: #0e6a2a;
    --green-deep: #0a4f1f;
    --ink: #151515;
    --paper: #fafafa;
    --canvas: #e4e4e4;
    --white: #ffffff;
  }
  * { margin: 0; padding: 0; box-sizing: border-box; }
  html, body { width: 1200px; height: 2522px; overflow: hidden; }
  body {
    background: var(--canvas);
    font-family: "Montserrat", Arial, sans-serif;
    color: var(--ink);
    position: relative;
  }
  .card {
    position: absolute;
    left: 98px;
    width: 1005px;
    height: 670px;
    overflow: hidden;
    background: var(--paper);
    box-shadow: 0 18px 30px rgba(0,0,0,.28);
  }
  .card--front { top: 551px; }
  .card--back { top: 1301px; background: var(--white); }
  .layer { position: absolute; left: 0; top: 0; width: 1005px; height: 670px; }
  .abs { position: absolute; }

  /* brand lockup */
  .brand { display: flex; align-items: center; gap: 14px; color: var(--green); font-weight: 700; }
  .brand__dot { width: 58px; height: 58px; border-radius: 50%; background: var(--green); flex: none; }
  .brand__name { font-size: 58px; line-height: 50px; letter-spacing: -1px; }
  .brand__tag { font-size: 19px; letter-spacing: 4.5px; line-height: 24px; }
  .front-brand { left: 30px; top: 34px; }

  .tagline-pill {
    left: 30px; top: 150px; height: 34px;
    display: flex; border-radius: 17px; overflow: hidden;
    font-size: 20px; font-weight: 800; color: var(--white);
    border: 2px solid var(--green-deep);
  }
  .tagline-pill span { padding: 0 12px; line-height: 30px; }
  .tagline-pill__brand { background: var(--green); }
  .tagline-pill__rest { background: var(--green-deep); }
  .supply-note {
    left: 30px; top: 189px; width: 355px;
    font-size: 14.5px; line-height: 20px; text-align: center; color: #333;
  }
  .supply-note b { font-weight: 600; color: var(--ink); }
  .supply-note .hl { color: var(--green); font-weight: 500; }

  .offer {
    left: 68px; top: 236px; width: 272px; height: 120px;
    border-left: 2px solid var(--green); border-right: 2px solid var(--green);
  }
  .offer::before, .offer::after {
    content: ""; position: absolute; left: 0; right: 0; height: 2px;
    background: linear-gradient(to right, var(--green) 18px, transparent 18px, transparent calc(100% - 18px), var(--green) 0);
  }
  .offer::before { top: 0; }
  .offer::after { bottom: 0; }
  .offer__amount { position: absolute; left: 28px; top: -2px; display: flex; align-items: flex-start; }
  .offer__num { font-size: 84px; font-weight: 900; color: var(--green); line-height: 84px; letter-spacing: -3px; }
  .offer__pct { font-size: 46px; font-weight: 800; color: var(--green); line-height: 46px; margin-top: 20px; margin-left: 4px; }
  .offer__off { font-size: 32px; font-weight: 800; color: var(--ink); line-height: 32px; margin-top: 30px; margin-left: 4px; }
  .offer__code {
    position: absolute; left: 30px; top: 80px; display: flex;
    font-size: 19px; font-weight: 500; line-height: 26px; color: var(--white);
  }
  .offer__code span { padding: 0 6px; background: var(--ink); }
  .offer__code b { padding: 0 6px; background: var(--green); font-weight: 500; }

  .products-title {
    left: 60px; top: 423px; width: 255px;
    display: flex; align-items: center; gap: 6px;
    color: var(--white); font-size: 17px; font-weight: 700;
  }
  .products-title::before, .products-title::after { content: ""; flex: 1; height: 1.5px; background: var(--white); }
  .product-list { list-style: none; top: 458px; color: var(--white); font-size: 15px; font-weight: 500; }
  .product-list--a { left: 30px; }
  .product-list--b { left: 240px; }
  .product-list li { height: 26px; line-height: 26px; display: flex; align-items: center; gap: 9px; }
  .product-list svg { width: 16px; height: 16px; flex: none; }

  .contact-pill {
    left: 30px; top: 626px; height: 30px; padding: 0 12px 0 6px;
    background: var(--white); border-radius: 15px;
    display: flex; align-items: center; gap: 6px;
    font-size: 16px; color: var(--ink);
  }
  .contact-pill svg { width: 20px; height: 20px; }
  .contact-pill .phone { color: var(--green); font-weight: 700; }
  .contact-pill .sep { margin: 0 4px; color: #555; }

  /* back */
  .back-headline {
    left: 30px; top: 30px; width: 450px;
    font-size: 26px; font-style: italic; font-weight: 700; line-height: 37px; color: var(--white);
  }
  .back-title {
    left: 30px; top: 158px;
    font-size: 50px; font-weight: 900; line-height: 56px; color: var(--white);
  }
  .back-copy {
    left: 30px; width: 405px;
    font-size: 13px; line-height: 17.5px; color: var(--white); text-align: justify;
  }
  .back-copy--one { top: 287px; }
  .back-copy--two { top: 367px; }
  .back-sub {
    left: 30px; top: 477px;
    font-size: 22px; font-weight: 800; line-height: 32px; color: var(--white);
  }
  .back-note { left: 30px; top: 541px; width: 320px; font-size: 13.5px; line-height: 19px; color: var(--white); }
  .back-contact { left: 34px; top: 592px; font-size: 19px; line-height: 30px; color: var(--white); }
  .back-contact b { font-weight: 700; }

  .back-brand {
    left: 630px; top: 30px; width: 180px;
    display: flex; flex-direction: column; align-items: center; color: var(--green); font-weight: 700;
  }
  .back-brand .brand__dot { width: 80px; height: 80px; margin-bottom: 20px; }
  .back-brand .brand__name { font-size: 36px; line-height: 36px; letter-spacing: -.5px; }
  .back-brand .brand__tag { font-size: 13.5px; letter-spacing: 2.5px; line-height: 18px; }

  .stamp-box { left: 848px; top: 38px; width: 140px; height: 140px; border: 1.5px solid #444; }
  .address-line { left: 662px; width: 326px; height: 1.5px; background: #555; }
</style>
</head>
<body>

<!-- FRONT -->
<section class="card card--front">
  <svg class="layer" viewBox="0 0 1005 670" aria-hidden="true">
    <path d="M0 398 C160 350 410 360 575 455 C625 490 640 560 620 670 H0 Z" fill="var(--green-dark)"/>
    <path d="M0 412 C160 366 405 376 565 468 C610 500 622 565 604 670 H0 Z" fill="var(--green)"/>
  </svg>

  <svg class="layer" viewBox="0 0 1005 670" role="img" aria-label="Photo of two masked shop workers holding a potted aloe plant and an Open sign among greenery">
    <defs>
      <linearGradient id="photoFront" x1="0" y1="0" x2="1" y2="1">
        <stop offset="0" stop-color="#5f8f3c"/>
        <stop offset=".5" stop-color="#3b6a2a"/>
        <stop offset="1" stop-color="#2b4a22"/>
      </linearGradient>
    </defs>
    <path d="M690 0 H1005 V670 H615 C590 600 640 520 700 430 C760 330 740 200 690 0 Z" fill="url(#photoFront)"/>
  </svg>

  <svg class="layer" viewBox="0 0 1005 670" role="img" aria-label="Photo of a box of blue nitrile gloves">
    <defs>
      <linearGradient id="photoGloves" x1="0" y1="0" x2="1" y2="1">
        <stop offset="0" stop-color="#e9f2f7"/>
        <stop offset="1" stop-color="#7fb2de"/>
      </linearGradient>
    </defs>
    <circle cx="520" cy="555" r="92" fill="#eef3ee"/>
    <circle cx="520" cy="555" r="80" fill="url(#photoGloves)"/>
  </svg>

  <div class="abs brand front-brand">
    <span class="brand__dot"></span>
    <div>
      <div class="brand__name">CAREVALE</div>
      <div class="brand__tag">MEDICAL SUPPLY</div>
    </div>
  </div>

  <div class="abs tagline-pill">
    <span class="tagline-pill__brand">CAREVALE</span><span class="tagline-pill__rest">IS HERE FOR YOU!</span>
  </div>
  <p class="abs supply-note">Supplies available nationwide from Hawai'i to <span class="hl">New York</span> and <b>everywhere</b> in between.</p>

  <div class="abs offer">
    <div class="offer__amount">
      <span class="offer__num">10</span><span class="offer__pct">%</span><span class="offer__off">OFF</span>
    </div>
    <div class="offer__code"><span>Promo Code:</span><b>10OFF</b></div>
  </div>

  <h2 class="abs products-title">OUR PRODUCTS</h2>
  <ul class="abs product-list product-list--a">
    <li><svg viewBox="0 0 16 16"><circle cx="8" cy="8" r="7" fill="none" stroke="#fff" stroke-width="1.6"/><path d="M4.5 8.2 7 10.6 11.6 5.6" fill="none" stroke="#fff" stroke-width="1.8"/></svg>Face Shields</li>
    <li><svg viewBox="0 0 16 16"><circle cx="8" cy="8" r="7" fill="none" stroke="#fff" stroke-width="1.6"/><path d="M4.5 8.2 7 10.6 11.6 5.6" fill="none" stroke="#fff" stroke-width="1.8"/></svg>Nitrile Gloves</li>
    <li><svg viewBox="0 0 16 16"><circle cx="8" cy="8" r="7" fill="none" stroke="#fff" stroke-width="1.6"/><path d="M4.5 8.2 7 10.6 11.6 5.6" fill="none" stroke="#fff" stroke-width="1.8"/></svg>Vinyl Gloves</li>
    <li><svg viewBox="0 0 16 16"><circle cx="8" cy="8" r="7" fill="none" stroke="#fff" stroke-width="1.6"/><path d="M4.5 8.2 7 10.6 11.6 5.6" fill="none" stroke="#fff" stroke-width="1.8"/></svg>Isolation Gowns</li>
    <li><svg viewBox="0 0 16 16"><circle cx="8" cy="8" r="7" fill="none" stroke="#fff" stroke-width="1.6"/><path d="M4.5 8.2 7 10.6 11.6 5.6" fill="none" stroke="#fff" stroke-width="1.8"/></svg>Gallon Hand Sanitizer</li>
    <li><svg viewBox="0 0 16 16"><circle cx="8" cy="8" r="7" fill="none" stroke="#fff" stroke-width="1.6"/><path d="M4.5 8.2 7 10.6 11.6 5.6" fill="none" stroke="#fff" stroke-width="1.8"/></svg>Black Kn95's</li>
  </ul>
  <ul class="abs product-list product-list--b">
    <li><svg viewBox="0 0 16 16"><circle cx="8" cy="8" r="7" fill="none" stroke="#fff" stroke-width="1.6"/><path d="M4.5 8.2 7 10.6 11.6 5.6" fill="none" stroke="#fff" stroke-width="1.8"/></svg>White Kn95's</li>
    <li><svg viewBox="0 0 16 16"><circle cx="8" cy="8" r="7" fill="none" stroke="#fff" stroke-width="1.6"/><path d="M4.5 8.2 7 10.6 11.6 5.6" fill="none" stroke="#fff" stroke-width="1.8"/></svg>4520 N95</li>
    <li><svg viewBox="0 0 16 16"><circle cx="8" cy="8" r="7" fill="none" stroke="#fff" stroke-width="1.6"/><path d="M4.5 8.2 7 10.6 11.6 5.6" fill="none" stroke="#fff" stroke-width="1.8"/></svg>4530 N95</li>
    <li><svg viewBox="0 0 16 16"><circle cx="8" cy="8" r="7" fill="none" stroke="#fff" stroke-width="1.6"/><path d="M4.5 8.2 7 10.6 11.6 5.6" fill="none" stroke="#fff" stroke-width="1.8"/></svg>Biohazard Bags</li>
    <li><svg viewBox="0 0 16 16"><circle cx="8" cy="8" r="7" fill="none" stroke="#fff" stroke-width="1.6"/><path d="M4.5 8.2 7 10.6 11.6 5.6" fill="none" stroke="#fff" stroke-width="1.8"/></svg>Puratex Wipes</li>
    <li><svg viewBox="0 0 16 16"><circle cx="8" cy="8" r="7" fill="none" stroke="#fff" stroke-width="1.6"/><path d="M4.5 8.2 7 10.6 11.6 5.6" fill="none" stroke="#fff" stroke-width="1.8"/></svg>and Kor Spray</li>
  </ul>

  <div class="abs contact-pill">
    <svg viewBox="0 0 20 20" aria-hidden="true"><circle cx="10" cy="10" r="9" fill="none" stroke="var(--green)" stroke-width="1.8"/><path d="M7 5.5 8.6 7.6 7.8 8.8C8.5 10.3 9.7 11.5 11.2 12.2L12.4 11.4 14.5 13 13.6 14.3C10 14 6 10 5.7 6.4Z" fill="var(--green)"/></svg>
    <span class="phone">808-241-7739</span>
    <span class="sep">|</span>
    <svg viewBox="0 0 20 20" aria-hidden="true"><circle cx="10" cy="10" r="9" fill="var(--green)"/><g fill="none" stroke="#fff" stroke-width="1.1"><circle cx="10" cy="10" r="5.5"/><ellipse cx="10" cy="10" rx="2.4" ry="5.5"/><path d="M4.5 10h11"/></g></svg>
    <span>www.carevale.shop</span>
  </div>
</section>

<!-- BACK -->
<section class="card card--back">
  <svg class="layer" viewBox="0 0 1005 670" aria-hidden="true">
    <path d="M0 0 H500 C560 120 640 260 592 385 C545 505 430 600 300 670 H0 Z" fill="var(--green)"/>
    <circle cx="540" cy="125" r="92" fill="#eef3ee"/>
    <circle cx="565" cy="325" r="80" fill="#eef3ee"/>
    <circle cx="497" cy="485" r="72" fill="#eef3ee"/>
  </svg>
  <svg class="layer" viewBox="0 0 1005 670" role="img" aria-label="Product photos: a blue isolation gown, a pair of white N95 respirators and a teal N95 respirator">
    <circle cx="540" cy="125" r="80" fill="#dbe8f4"/>
    <circle cx="565" cy="325" r="68" fill="#f2f2ec"/>
    <circle cx="497" cy="485" r="60" fill="#cfe7e6"/>
  </svg>

  <p class="abs back-headline">25 Years Strong - Home Care, Senior Living, PPE, Medical, &amp; Healthcare Supplies....</p>
  <h2 class="abs back-title">WHY<br>CHOOSE US?</h2>
  <p class="abs back-copy back-copy--one">Carevale's sudden rise as a supplier of PPE, medical, and healthcare products during the COVID-19 pandemic in 2020 actually began 25 years earlier as part of Maren Okafor's longtime commitment to helping people.</p>
  <p class="abs back-copy back-copy--two">Carevale maintains a supply of all types of safety, health, and wellness items for businesses, schools, hospitals, government agencies, and households. If there's something specific that you need, we will find it for you.</p>
  <h3 class="abs back-sub">CAN'T FIND WHAT<br>YOU ARE LOOKING FOR?</h3>
  <p class="abs back-note">If you need a different size or product than what you see here email us at:</p>
  <p class="abs back-contact">info@<b>carevale</b>.shop<br>or Call Us at <b>808-241-7739</b></p>

  <div class="abs back-brand">
    <span class="brand__dot"></span>
    <div class="brand__name">CAREVALE</div>
    <div class="brand__tag">MEDICAL SUPPLY</div>
  </div>

  <div class="abs stamp-box"></div>
  <div class="abs address-line" style="top:410px"></div>
  <div class="abs address-line" style="top:484px"></div>
  <div class="abs address-line" style="top:557px"></div>
</section>

</body>
</html>
```